Business Card Design Project

Business Card
We are rebranding with a new logo
Industry/Entity Type
Business
Contact Information for Business Card
Dennis Marlow +61 427581962 dennis@qovo.com.au P.O. Box 872 Kelvindale QLD 4309
Requirements
Must have
- Logo

```html
<!DOCTYPE html>
<html lang="en">
<head>
<meta charset="utf-8">
<title>Qovo International – Business Card</title>
<link rel="stylesheet" href="https://fonts.googleapis.com/css2?family=Ubuntu:wght@400;500;700&display=swap">
<style>
  :root {
    --backdrop: #dcdcdc;
    --card-white: #f4f4f2;
    --brand-blue: #0a9bd2;
    --brand-orange: #e07b21;
    --brand-navy: #0e6a97;
    --ink-light: #ffffff;
  }
  html, body {
    margin: 0;
    width: 1200px;
    height: 899px;
    overflow: hidden;
    background: var(--backdrop);
    font-family: "Ubuntu", Arial, sans-serif;
  }
  .stage { position: relative; width: 1200px; height: 899px; }
  .card {
    position: absolute;
    width: 560px;
    height: 320px;
    background: var(--card-white);
    box-shadow: 0 14px 30px rgba(0,0,0,.18);
    overflow: hidden;
  }
  .card svg.art { position: absolute; inset: 0; width: 100%; height: 100%; }
  .card--front { left: 110px; top: 100px; }
  .card--back { left: 530px; top: 480px; }

  .brand-name {
    position: absolute;
    margin: 0;
    color: var(--brand-navy);
    font-weight: 700;
    text-align: center;
    line-height: 1;
  }
  .brand-name .word-main { display: block; font-size: 58px; letter-spacing: 1px; }
  .brand-name .word-sub { display: block; font-size: 15px; letter-spacing: 4px; margin-top: 6px; }
  .card--front .brand-name { left: 170px; top: 62px; width: 260px; }
  .card--back .brand-name { left: 365px; top: 100px; width: 190px; }
  .card--back .brand-name .word-main { font-size: 50px; }
  .card--back .brand-name .word-sub { font-size: 13px; letter-spacing: 3px; }

  .contact-list {
    position: absolute;
    left: 40px;
    top: 70px;
    margin: 0;
    padding: 0;
    list-style: none;
    color: var(--ink-light);
    font-size: 15px;
  }
  .contact-list li {
    display: flex;
    align-items: center;
    gap: 16px;
    min-height: 36px;
    margin-bottom: 10px;
  }
  .contact-list .icon {
    flex: none;
    width: 34px;
    height: 34px;
    border-radius: 50%;
    background: var(--brand-orange);
    display: flex;
    align-items: center;
    justify-content: center;
  }
  .contact-list .icon svg { width: 18px; height: 18px; }
  .contact-name { font-weight: 700; font-size: 16px; }
  .contact-address { line-height: 1.2; }
</style>
</head>
<body>
<main class="stage">

  <section class="card card--front" aria-label="Card front">
    <svg class="art" viewBox="0 0 560 320" preserveAspectRatio="none" aria-hidden="true">
      <rect class="tab" x="300" y="0" width="160" height="16" fill="var(--brand-blue)"/>
      <path class="sweep-blue" d="M0,40 C140,200 340,250 560,215 V320 H0 Z" fill="var(--brand-blue)"/>
      <path class="sweep-orange" d="M0,40 C140,200 340,250 560,215 V238 C340,258 140,215 0,44 Z" fill="var(--brand-orange)"/>
      <path class="sweep-white" d="M0,0 H560 V215 C340,250 140,200 0,40 Z" fill="var(--card-white)"/>
      <rect x="300" y="0" width="160" height="16" fill="var(--brand-blue)"/>
    </svg>
    <p class="brand-name"><span class="word-main">Qovo</span><span class="word-sub">INTERNATIONAL</span></p>
  </section>

  <section class="card card--back" aria-label="Card back">
    <svg class="art" viewBox="0 0 560 320" preserveAspectRatio="none" aria-hidden="true">
      <rect width="560" height="320" fill="var(--brand-blue)"/>
      <path class="crescent-orange" d="M335,0 C300,110 330,240 405,320 H560 V0 Z" fill="var(--brand-orange)"/>
      <path class="crescent-white" d="M365,0 C335,110 380,240 470,320 H560 V0 Z" fill="var(--card-white)"/>
    </svg>

    <ul class="contact-list">
      <li>
        <span class="icon"><svg viewBox="0 0 20 20"><circle cx="10" cy="7" r="4" fill="#fff"/><path d="M3,18 C3,12 17,12 17,18 Z" fill="#fff"/></svg></span>
        <span class="contact-name">Dennis Marlow</span>
      </li>
      <li>
        <span class="icon"><svg viewBox="0 0 20 20"><circle cx="10" cy="10" r="7.5" fill="none" stroke="#fff" stroke-width="1.6"/><path d="M7,6 L8.6,6 L9.4,8.2 L8.4,9.2 C9,10.6 9.6,11.2 11,11.8 L12,10.8 L14,11.6 L14,13.2 C10,14 6,10 7,6 Z" fill="#fff"/></svg></span>
        <span>+61 427581962</span>
      </li>
      <li>
        <span class="icon"><svg viewBox="0 0 20 20"><path d="M10,3 L18,10 H15.5 V17 H11.5 V13 H8.5 V17 H4.5 V10 H2 Z" fill="#fff"/></svg></span>
        <span class="contact-address">P.O. Box 872<br>Kelvindale QLD 4309</span>
      </li>
      <li>
        <span class="icon"><svg viewBox="0 0 20 20" fill="none" stroke="#fff" stroke-width="1.4"><circle cx="10" cy="10" r="7"/><ellipse cx="10" cy="10" rx="3" ry="7"/><path d="M3,10 H17 M4.2,6.5 H15.8 M4.2,13.5 H15.8"/></svg></span>
        <span>dennis@qovo.com.au</span>
      </li>
    </ul>

    <p class="brand-name"><span class="word-main">Qovo</span><span class="word-sub">INTERNATIONAL</span></p>
  </section>

</main>
</body>
</html>
```